Plate Parade! Digital Order Web App

This is a web app on mobile phone, for consumers to order food inside a restaurant using their phones. we have done up the flow but we need to revamp UI design. pls have a look at our current web on your mobile phone:
https://demo.pesanly.app/o/KWLM/274615

CURRENT DESIGN.
1. food category on left side, always shown. menu items in list view with image.
2. when we click on an item, there is popup page, to select modifiers, or quantity.
3. order review page(cart page) is quite messy now, need a complete new look.
4 payment page(no need to design, handle by Paxtel)
5. order confirmation page. success or error return

DESIGN requirements:
please browse through and click to order with current page above. we have put in lots of thoughts and effort for current flow, the new design should base on this flow.
1. web app. no zoom in/out is allowed for users. responsive html to suit different mobile phone screen size. modern fonts.
2. PAGES needed:
home/welcome page,
well laid out menu items page,
single item page, with add on choice and modifier
cart page(to include recommended items, ordered item list, remove item total, changeable quantity,
confirmation page(success, fail)

DELIVERABLES - responsive html, fonts, images asset such as icons, animation, button images(suitable for commercial use without further third party loyalty fee)

Hi all if we have left a comment on ur design, please revise accordingly and we will conclude it soon!

Target Market(s)

young diners who order food on their mobile phone.

Industry/Entity Type

Restaurant

Coding

Coded - Design and coding required

Number of Pages Required

5+ page

Colors

Designer to choose colors to be used in the design.

Requirements
Must have
• - lively, appetising colors while making the page easy to read. easy on eyes.
• - consistency. fonts used.
Nice to have
• - 2 color schemes
• - html codes. we will top up if you can deliver coded html.
Should not have
• - should not have more than 3 colors
• - should not have more than 3 different fonts
• - should not use colors that are dull

```html
<!DOCTYPE html>
<html lang="en">
<head>
<meta charset="utf-8">
<meta name="viewport" content="width=783, user-scalable=no">
<title>Plate Parade! – Menu</title>
<link href="https://fonts.googleapis.com/css2?family=Montserrat:wght@600;700;800&family=Open+Sans:wght@400;600;700&display=swap" rel="stylesheet">
<style>
  :root{
    --sidebar:#2f3031;
    --sidebar-deep:#232425;
    --accent:#7dd3d6;
    --pink:#e3157f;
    --ink:#2a2a2a;
    --muted:#6d6d6d;
    --card:#ffffff;
    --page:#f1f2ef;
  }
  *{box-sizing:border-box;margin:0;padding:0}
  html,body{width:783px;height:1200px;overflow:hidden}
  body{font-family:"Open Sans",sans-serif;background:var(--page);color:var(--ink)}
  .app{display:flex;width:783px;height:1200px}
  .sidebar{width:250px;flex:none;height:100%;background:linear-gradient(180deg,var(--sidebar) 0%,var(--sidebar-deep) 100%);color:#fff;padding-top:70px}
  .brand{font-family:"Montserrat",sans-serif;font-weight:800;font-size:26px;letter-spacing:1px;padding-left:32px;white-space:nowrap}
  .menu-toggle{display:block;margin:16px 0 0 84px}
  .categories{list-style:none;margin-top:34px}
  .category{display:flex;align-items:center;gap:18px;height:58px;padding-left:32px;font-size:15px;font-weight:600;color:#e8e8e8}
  .category svg{flex:none}
  .category.is-active{background:var(--accent);color:#fff}
  .content{flex:1;position:relative;padding:84px 20px 0 20px;
    background:radial-gradient(circle at 80% 20%,#fbfbf8 0%,#eef1ea 40%,#f4f1ec 75%,#ecefe8 100%)}
  .section-title{font-family:"Montserrat",sans-serif;font-weight:700;font-size:24px;margin-bottom:24px}
  .dish{display:flex;height:150px;margin-bottom:22px;box-shadow:0 4px 12px rgba(0,0,0,.12)}
  .dish-photo{width:150px;height:150px;flex:none}
  .dish-body{flex:1;min-width:0;background:var(--card);padding:22px 18px}
  .dish-name{font-weight:700;font-size:16px;line-height:1.3;color:var(--ink);white-space:nowrap}
  .dish-note{font-size:14px;color:var(--muted);margin-top:6px}
  .dish-price{display:inline-block;margin-top:14px;background:var(--pink);color:#fff;font-size:12px;font-weight:700;padding:5px 14px;border-radius:2px}
</style>
</head>
<body>
<div class="app">
  <aside class="sidebar">
    <div class="brand">NOVRIK</div>
    <svg class="menu-toggle" width="34" height="22" viewBox="0 0 34 22"><g stroke="#fff" stroke-width="3" stroke-linecap="round"><line x1="2" y1="3" x2="32" y2="3"/><line x1="2" y1="11" x2="32" y2="11"/><line x1="2" y1="19" x2="32" y2="19"/></g></svg>
    <ul class="categories">
      <li class="category is-active"><svg width="20" height="20" viewBox="0 0 20 20"><path d="M4 16 C4 8 10 3 17 3 C17 10 12 16 4 16Z" fill="none" stroke="#fff" stroke-width="2"/></svg>Vegetable</li>
      <li class="category"><svg width="20" height="20" viewBox="0 0 20 20"><ellipse cx="10" cy="10" rx="7" ry="5" fill="none" stroke="#fff" stroke-width="2"/></svg>Meat</li>
      <li class="category"><svg width="20" height="20" viewBox="0 0 20 20"><path d="M2 10 Q9 3 15 10 Q9 17 2 10Z M15 10 L19 6 L19 14Z" fill="none" stroke="#fff" stroke-width="2"/></svg>Seafood</li>
      <li class="category"><svg width="20" height="20" viewBox="0 0 20 20"><path d="M10 2 L12.4 7.5 L18 8 L13.7 11.8 L15 17.5 L10 14.5 L5 17.5 L6.3 11.8 L2 8 L7.6 7.5Z" fill="none" stroke="#fff" stroke-width="1.8"/></svg>Special</li>
      <li class="category"><svg width="20" height="20" viewBox="0 0 20 20"><g stroke="#fff" stroke-width="2"><line x1="10" y1="2" x2="10" y2="18"/><line x1="3" y1="6" x2="17" y2="14"/><line x1="3" y1="14" x2="17" y2="6"/></g></svg>Cold Dish</li>
      <li class="category"><svg width="20" height="20" viewBox="0 0 20 20"><path d="M2 9 H18 A8 8 0 0 1 2 9Z" fill="none" stroke="#fff" stroke-width="2"/></svg>Main</li>
      <li class="category"><svg width="20" height="20" viewBox="0 0 20 20"><rect x="3" y="3" width="14" height="14" rx="2" fill="none" stroke="#fff" stroke-width="2"/></svg>Set</li>
      <li class="category"><svg width="20" height="20" viewBox="0 0 20 20"><path d="M5 4 H15 L13 18 H7Z" fill="none" stroke="#fff" stroke-width="2"/></svg>Juice</li>
      <li class="category"><svg width="20" height="20" viewBox="0 0 20 20"><path d="M4 5 H14 V14 A3 3 0 0 1 11 17 H7 A3 3 0 0 1 4 14Z M14 8 H17 V12 H14" fill="none" stroke="#fff" stroke-width="2"/></svg>Drink</li>
      <li class="category"><svg width="20" height="20" viewBox="0 0 20 20"><path d="M5 3 H13 V17 H5Z M13 6 H16 V13 H13" fill="none" stroke="#fff" stroke-width="2"/></svg>Beer</li>
      <li class="category"><svg width="20" height="20" viewBox="0 0 20 20"><path d="M8 2 H12 V6 L14 9 V18 H6 V9 L8 6Z" fill="none" stroke="#fff" stroke-width="2"/></svg>Alcohol</li>
      <li class="category"><svg width="20" height="20" viewBox="0 0 20 20"><path d="M5 2 H15 Q15 10 10 10 Q5 10 5 2Z M10 10 V17 M6 18 H14" fill="none" stroke="#fff" stroke-width="2"/></svg>Wine</li>
    </ul>
  </aside>

  <main class="content">
    <h1 class="section-title">Vegetable</h1>

    <article class="dish">
      <div class="dish-photo" role="img" aria-label="Photo of grilled romaine lettuce" style="background:linear-gradient(135deg,#5a7a2c,#a8b94a 55%,#6b4a22)"></div>
      <div class="dish-body"><h2 class="dish-name">Grilled Romaine Lettuce</h2><p class="dish-note">Crisp greens</p><span class="dish-price">$4.80</span></div>
    </article>

    <article class="dish">
      <div class="dish-photo" role="img" aria-label="Photo of grilled oyster mushroom skewers" style="background:linear-gradient(135deg,#7a4a24,#b8834a 55%,#4a2a14)"></div>
      <div class="dish-body"><h2 class="dish-name">Grilled Oyster Mushroom</h2><p class="dish-note">Smoky mushroom</p><span class="dish-price">$5.20</span></div>
    </article>

    <article class="dish">
      <div class="dish-photo" role="img" aria-label="Photo of grilled shiitake mushroom skewers" style="background:linear-gradient(135deg,#5a3418,#9a5a2a 55%,#3a2010)"></div>
      <div class="dish-body"><h2 class="dish-name">Grilled Shiitake Mushroom</h2><p class="dish-note">Savory shiitake</p><span class="dish-price">$5.20</span></div>
    </article>

    <article class="dish">
      <div class="dish-photo" role="img" aria-label="Photo of grilled king oyster mushroom with herbs" style="background:linear-gradient(135deg,#c9b48a,#8aa040 55%,#6a4a2a)"></div>
      <div class="dish-body"><h2 class="dish-name">Grilled Pleurotus Eryngii</h2><p class="dish-note">King mushroom</p><span class="dish-price">$5.60</span></div>
    </article>

    <article class="dish">
      <div class="dish-photo" role="img" aria-label="Photo of grilled potato slices" style="background:linear-gradient(135deg,#e0a830,#c87a1a 55%,#5a3614)"></div>
      <div class="dish-body"><h2 class="dish-name">Grilled Potato Chip 3Pcs</h2><p class="dish-note">Golden potato</p><span class="dish-price">$3.90</span></div>
    </article>

    <article class="dish">
      <div class="dish-photo" role="img" aria-label="Photo of grilled dry bean curd pieces" style="background:linear-gradient(135deg,#d9a04a,#a8702a 55%,#4a3018)"></div>
      <div class="dish-body"><h2 class="dish-name">Grilled Dry Soya Bean Cake 3Pcs</h2><p class="dish-note">Tofu bites</p><span class="dish-price">$3.90</span></div>
    </article>
  </main>
</div>
</body>
</html>
```